Business Cards Needed for Innovative Healthcare Marketing Company

We are a marketing company focused on healthcare. Our company is all about rebranding yourself renewing your image and generating results. The phoenix stands for "reborn" or "rising" which we provide new brands for our clients we take their old brands and renew it with creativity and innovation. I am looking for a business card with color dimension. I have attached an example of a card I think has the look and feel of what I am trying to accomplish. I like that the card example has black and grey font colors, I like the font placement and the small logo, I really like the use of the colors on the right those are the colors of my logo. My logo is phoenix so maybe incorporating flames similar to that design. I would like the back a solid color maybe red with an opaque version of the logo and website. As a marketing company I am always open to creative liberty!

Target Market(s)

Doctors and business professionals.

Industry/Entity Type

Marketing

Contact Information for Business Card

Velmora Health Care Marketing
Dana Prewitt- CEO
#(407)555-0172
email-dana@velmora.com
website- velmora.com

Font styles to use
Sans Serif

Colors
ec1f27
f37122
ffc214
fbed22
fbf289
f04a50

Requirements
Must have
• The logo and required information
Nice to have
• icons by the information
Should not have
• child like font

```html
<!DOCTYPE html>
<html lang="en">
<head>
<meta charset="utf-8">
<title>Dana Prewitt – Business Card</title>
<link rel="stylesheet" href="https://fonts.googleapis.com/css2?family=Arimo:wght@400;700&display=swap">
<style>
  :root {
    --brand-red: #c9372c;
    --ink: #111111;
    --muted-grey: #a6a6a6;
    --faint-grey: #ededed;
    --flame-orange: #f37122;
    --flame-yellow: #ffc214;
    --paper: #ffffff;
  }
  * { margin: 0; padding: 0; box-sizing: border-box; }
  html, body { width: 1200px; height: 600px; overflow: hidden; background: var(--paper); }
  body { font-family: "Arimo", Arial, sans-serif; }
  .card { position: relative; width: 1200px; height: 600px; background: var(--paper); }

  .identity { position: absolute; left: 66px; top: 78px; }
  .identity__name { font-size: 80px; font-weight: 700; color: var(--brand-red); line-height: 1; letter-spacing: 0.5px; }
  .identity__title { margin-top: 14px; font-size: 38px; font-weight: 400; color: var(--muted-grey); line-height: 1; }

  .contact { position: absolute; left: 66px; top: 408px; list-style: none; }
  .contact__item { font-size: 30px; color: var(--ink); line-height: 53px; }

  .decor-stethoscope {
    position: absolute; left: 860px; top: 34px; width: 308px; height: 358px;
    border-radius: 40px;
    background: linear-gradient(180deg, var(--faint-grey), #f6f6f6);
  }

  .brand { position: absolute; left: 752px; top: 400px; display: flex; align-items: center; gap: 24px; }
  .brand__mark { width: 136px; height: 136px; border-radius: 50%;
    background: radial-gradient(circle at 50% 40%, var(--flame-yellow), var(--flame-orange)); }
  .brand__name { color: var(--brand-red); font-weight: 400; line-height: 1; }
  .brand__word { display: block; font-size: 52px; letter-spacing: 2px; }
  .brand__rule { display: block; height: 2px; margin: 10px 0 8px; background: var(--brand-red); }
  .brand__tagline { display: block; font-size: 18px; letter-spacing: 0.6px; }
</style>
</head>
<body>
  <main class="card">
    <header class="identity">
      <h1 class="identity__name">Dana Prewitt</h1>
      <p class="identity__title">CEO</p>
    </header>

    <ul class="contact">
      <li class="contact__item">#(407)555-0172</li>
      <li class="contact__item">Email: dana@velmora.com</li>
      <li class="contact__item">Website: www.velmora.com</li>
    </ul>

    <div class="decor-stethoscope" role="img" aria-label="Faint grey stethoscope decoration"></div>

    <div class="brand">
      <div class="brand__mark"></div>
      <p class="brand__name">
        <span class="brand__word">VELMORA</span>
        <span class="brand__rule"></span>
        <span class="brand__tagline">HEALTH CARE MARKETING</span>
      </p>
    </div>
  </main>
</body>
</html>
```